Lindenkrügelhof airline passengers needs web site design

We need a website design (and a logo) for a new charity based in Switzerland. We are helping airline passengers to receive the compensation they are entiteld to by european law from the airlines in cases of delays or denied boarding or cancelled flights. Airlines often try to not pay those compensations so the passengers need assistance in receiving the compensations.

Target Market(s)

Switzerland

Industry/Entity Type

Charity

Logo Text

lindenkrügelhof.ch

Number of Pages Required

1 page

Colors

Designer to choose colors to be used in the design.

```html
<!DOCTYPE html>
<html lang="en">
<head>
<meta charset="utf-8">
<title>Lindenkrügelhof – Airline Passengers</title>
<link href="https://fonts.googleapis.com/css2?family=Raleway:wght@400;500;600&family=Roboto:wght@400;500;700&family=Oswald:wght@400&display=swap" rel="stylesheet">
<style>
:root{
  --blue:#0f72c2;
  --blue-dark:#0b5aa0;
  --nav-top:#2a86d8;
  --nav-bottom:#0c5fae;
  --orange:#e8531a;
  --light-blue:#6fb7de;
  --text:#333;
  --muted:#555;
  --rule:#dcdcdc;
  --footer:#2c2c2c;
  --footer-head:#4aa3d8;
  --white:#fff;
}
*{box-sizing:border-box;margin:0;padding:0}
html,body{width:1200px;height:2206px;overflow:hidden;background:var(--white)}
body{font-family:'Roboto',sans-serif;color:var(--text);position:relative}
.wrap{position:relative;width:1054px;margin:0 auto}

/* header */
.site-header{height:96px;position:relative}
.brand{position:absolute;left:73px;top:26px;display:flex;align-items:center;gap:12px}
.brand-mark{width:16px;height:16px;border-radius:50%;background:var(--orange)}
.brand-name{font-family:'Raleway',sans-serif;font-weight:600;font-size:24px;color:var(--blue)}
.brand-sub{font-family:'Raleway',sans-serif;font-size:22px;color:#444;padding-left:14px;margin-left:4px;border-left:1px solid #ccc;line-height:38px}
.header-actions{position:absolute;right:73px;top:29px;display:flex;gap:6px}
.social-box{width:37px;height:37px;background:#3b3b3b}
.btn-donate{height:37px;padding:0 17px;background:var(--orange);color:var(--white);font-family:'Oswald',sans-serif;font-size:17px;line-height:37px;margin-left:6px;text-transform:uppercase}

.main-nav{height:46px;background:linear-gradient(var(--nav-top),var(--nav-bottom));display:flex;padding-left:80px}
.main-nav a{color:var(--white);text-decoration:none;font-family:'Roboto',sans-serif;font-weight:500;font-size:16px;line-height:46px;padding:0 23px;border-right:1px solid rgba(0,0,0,.18)}
.main-nav a:last-child{border-right:none}

/* hero */
.hero{height:587px;position:relative;background:linear-gradient(180deg,#1d4f9c 0%,#2f6fbd 40%,#6d8ab0 62%,#c99a7a 78%,#8a5a3e 100%);text-align:center}
.hero h1{font-family:'Raleway',sans-serif;font-weight:400;font-size:32px;line-height:36px;color:var(--white);padding-top:44px}
.hero .btn-outline{display:inline-block;margin-top:20px;border:1px solid var(--white);background:var(--blue);color:var(--white);font-family:'Oswald',sans-serif;font-size:17px;padding:0 24px;line-height:46px;text-transform:uppercase}

/* welcome */
.welcome{height:374px;text-align:center;padding-top:40px}
.section-title{font-family:'Raleway',sans-serif;font-weight:500;font-size:28px;color:#222}
.section-title span{color:var(--blue)}
.title-rule{width:330px;height:1px;background:var(--rule);margin:12px auto 0;position:relative}
.title-rule::after{content:"";position:absolute;left:145px;top:-1px;width:40px;height:3px;background:var(--blue)}
.welcome p{font-size:13.6px;line-height:24px;color:var(--muted);width:1050px;margin:22px auto 0}
.welcome p + p{margin-top:24px}
.read-more{display:inline-block;font-size:13px;font-weight:700;color:#333;margin-top:14px;text-transform:uppercase}
.read-more::after{content:" ▸"}

/* mission */
.mission{height:347px;background:linear-gradient(90deg,#3c2a1c 0%,#5b3f2a 30%,#4a3322 60%,#2e2016 100%);text-align:center;color:var(--white)}
.mission h2{font-family:'Raleway',sans-serif;font-weight:500;font-size:26px;padding-top:62px}
.mission p{font-family:'Raleway',sans-serif;font-size:19.5px;line-height:33px;width:920px;margin:16px auto 0}

/* news + testimonials */
.updates{height:480px;position:relative}
.news{position:absolute;left:73px;top:42px;width:332px}
.col-title{font-family:'Raleway',sans-serif;font-weight:500;font-size:24px;color:#222;padding-bottom:6px;border-bottom:1px solid var(--rule)}
.news-item{display:flex;gap:12px;padding:18px 0 14px;border-bottom:1px solid #e6e6e6;height:83px}
.date-box{width:53px;height:53px;background:var(--light-blue);color:var(--white);text-align:center;flex:none;border:1px solid #e6f2f9}
.date-box .m,.date-box .y{font-size:9px;line-height:10px;display:block;padding-top:3px}
.date-box .d{font-size:22px;font-weight:700;line-height:22px;display:block}
.date-box .y{padding-top:0}
.news-item p{font-size:13.5px;line-height:22px;color:#333}
.news .read-more{margin-top:16px}

.reviews{position:absolute;left:433px;top:42px;width:694px}
.arrows{position:absolute;right:0;top:4px;display:flex;gap:3px}
.arrows svg{width:19px;height:19px}
.cards{display:flex;gap:27px;margin-top:18px}
.card{width:332px;height:341px;border:1px solid #ddd;position:relative;background:var(--white)}
.card blockquote{font-family:'Raleway',sans-serif;font-size:16px;line-height:24.5px;color:#666;padding:20px 22px 0}
.card-foot{position:absolute;left:-1px;right:-1px;bottom:-1px;height:109px;background:var(--blue);color:var(--white);text-align:center;padding-top:48px}
.avatar{position:absolute;left:50%;top:-46px;margin-left:-45px;width:90px;height:90px;border-radius:50%;background:linear-gradient(#c9b7a6,#7d6a5c);border:4px solid var(--white);box-shadow:0 0 0 2px var(--blue)}
.card-foot strong{display:block;font-size:17px;font-weight:700}
.card-foot span{font-size:16px}

/* footer */
.site-footer{height:283px;background:var(--footer);position:relative;color:#e6e6e6}
.f-col{position:absolute;top:48px}
.f-brand{left:73px;top:50px;text-align:center;width:150px}
.f-brand .brand-name{font-size:20px}
.f-brand .sub{display:block;font-family:'Raleway',sans-serif;font-size:22px;color:#aaa;line-height:24px;margin-top:14px}
.f-head{font-size:12.5px;color:var(--footer-head);text-transform:uppercase;letter-spacing:.4px;margin-bottom:22px}
.f-col p,.f-col li{font-size:13px;line-height:20px}
.f-contact{left:275px}
.f-contact p + p{margin-top:20px}
.f-news{left:503px;width:260px}
.email-field{margin-top:18px;width:256px;height:33px;background:var(--white);border:1px solid #999;color:#666;font-size:13px;line-height:31px;padding-left:12px;position:relative}
.email-field svg{position:absolute;right:6px;top:6px}
.f-links{left:796px}
.f-links ul{list-style:none;display:grid;grid-template-columns:103px 100px;row-gap:6px}
.f-connect{left:995px}
.f-connect .boxes{display:flex;gap:6px;margin-top:-2px}
.f-connect .boxes div{width:38px;height:38px;background:var(--white)}
.f-bottom{position:absolute;left:73px;right:73px;top:222px;border-top:1px solid #3e3e3e;padding-top:16px;display:flex;justify-content:space-between;font-size:12.5px;color:var(--footer-head);text-transform:uppercase;letter-spacing:.4px}
</style>
</head>
<body>

<header class="site-header">
  <div class="brand">
    <div class="brand-mark"></div>
    <div class="brand-name">Lindenkrügelhof</div>
    <div class="brand-sub">Airline Passengers</div>
  </div>
  <div class="header-actions">
    <div class="social-box"></div>
    <div class="social-box"></div>
    <div class="btn-donate">Donate Now</div>
  </div>
</header>

<nav class="main-nav">
  <a href="#">HOME</a><a href="#">ABOUT US</a><a href="#">PASSENGERS</a><a href="#">VOLUNTEERS</a><a href="#">EVENTS</a><a href="#">PARTICIPATION</a><a href="#">NEWS</a><a href="#">CONTACT US</a>
</nav>

<section class="hero" role="img" aria-label="Photo of many raised open hands against a blue sky">
  <h1>Lorem Ipsum Dolor Sit Amet,<br>Consectetur Adipiscing Elit,</h1>
  <span class="btn-outline">Donate Now</span>
</section>

<section class="welcome">
  <h2 class="section-title">Welcome to <span>Lindenkrügelhof Airline Passengers</span></h2>
  <div class="title-rule"></div>
  <p>Lorem Ipsum is simply dummy text of the printing and typesetting industry. Lorem Ipsum has been the industry's standard dummy text ever since the 1500s, when an unknown printer took a galley of type and scrambled it to make a type specimen book. It has survived not only five centuries, but also the leap into electronic typesetting, remaining essentially unchanged. It was popularised in the 1960s with the release of Letraset sheets containing Lorem Ipsum passages, and more recently with desktop publishing software like Aldus PageMaker including versions of Lorem Ipsum.</p>
  <p>Lorem ipsum dolor sit amet, consectetur adipiscing elit, sed do eiusmod tempor incididunt ut labore et dolore magna aliqua. Ut enim ad minim veniam, quis nostrud exercitation ullamco laboris nisi ut aliquip ex ea commodo consequat. Duis aute irure dolor in reprehenderit in voluptate velit esse cillum dolore eu fugiat nulla pariatur. Excepteur sint occaecat cupidatat non proident, sunt in culpa qui officia deserunt mollit anim id est laborum.</p>
  <span class="read-more">Read More</span>
</section>

<section class="mission" role="img" aria-label="Photo of a glass donation jar with coins on a wooden table, darkened">
  <h2>Our Mission</h2>
  <p>Lorem ipsum dolor sit amet, consectetur adipiscing elit, sed do eiusmod tempor incididunt ut labore et dolore magna aliqua. Ut enim ad minim veniam, quis nostrud exercitation ullamco laboris nisi ut aliquip ex ea commodo consequat. Lorem ipsum dolor sit amet, consectetur adipiscing elit, sed do eiusmod tempor incididunt ut labore et dolore magna aliqua. Ut enim ad minim veniam, quis nostrud exercitation ullamco laboris nisi ut aliquip ex ea commodo consequat.</p>
</section>

<section class="updates">
  <div class="news">
    <h3 class="col-title">Latest News</h3>
    <div class="news-item"><div class="date-box"><span class="m">JUL</span><span class="d">25</span><span class="y">2017</span></div><p>Lorem ipsum dolor sit amet, consectetur adipiscing elit,</p></div>
    <div class="news-item"><div class="date-box"><span class="m">JUL</span><span class="d">23</span><span class="y">2017</span></div><p>Lorem ipsum dolor sit amet, consectetur adipiscing elit,</p></div>
    <div class="news-item"><div class="date-box"><span class="m">JUL</span><span class="d">20</span><span class="y">2017</span></div><p>Lorem ipsum dolor sit amet, consectetur adipiscing elit,</p></div>
    <div class="news-item"><div class="date-box"><span class="m">JUL</span><span class="d">18</span><span class="y">2017</span></div><p>Lorem ipsum dolor sit amet, consectetur adipiscing elit,</p></div>
    <span class="read-more">Read More</span>
  </div>

  <div class="reviews">
    <h3 class="col-title">What People Are Saying About Us</h3>
    <div class="arrows">
      <svg viewBox="0 0 20 20"><circle cx="10" cy="10" r="8.5" fill="none" stroke="#0f72c2" stroke-width="1.5"/><path d="M11.5 6 7.5 10l4 4" fill="none" stroke="#0f72c2" stroke-width="1.8"/></svg>
      <svg viewBox="0 0 20 20"><circle cx="10" cy="10" r="8.5" fill="none" stroke="#0f72c2" stroke-width="1.5"/><path d="M8.5 6l4 4-4 4" fill="none" stroke="#0f72c2" stroke-width="1.8"/></svg>
    </div>
    <div class="cards">
      <article class="card">
        <blockquote>“Lorem ipsum dolor sit amet, consectetur adipiscing elit, sed do eiusmod tempor incididunt ut labore et dolore magna aliqua. Ut enim ad minim veniam, quis nostrud aliquip ex ea commodo consequat.”</blockquote>
        <div class="card-foot"><div class="avatar" role="img" aria-label="Portrait photo of Mara Keller"></div><strong>Mara Keller</strong><span>Lorem ipsum dolor</span></div>
      </article>
      <article class="card">
        <blockquote>“Lorem ipsum dolor sit amet, consectetur adipiscing elit, sed do eiusmod tempor incididunt ut labore et dolore magna aliqua. Ut enim ad minim veniam, quis nostrud aliquip ex ea commodo consequat.”</blockquote>
        <div class="card-foot"><div class="avatar" role="img" aria-label="Portrait photo of Luca Brunner"></div><strong>Luca Brunner</strong><span>Lorem ipsum dolor</span></div>
      </article>
    </div>
  </div>
</section>

<footer class="site-footer">
  <div class="f-col f-brand">
    <div class="brand-name">Lindenkrügelhof</div>
    <span class="sub">Airline<br>Passengers</span>
  </div>
  <div class="f-col f-contact">
    <div class="f-head">Contact Us</div>
    <p>857 Lorem ipsum dolor<br>Sit Amet, Suite 2A</p>
    <p>Phone: 100 000 000<br>Email: info@lindenkruegelhof.ch</p>
  </div>
  <div class="f-col f-news">
    <div class="f-head">Subscribe to our Newsletter</div>
    <p>Lorem ipsum dolor sit amet, conse ctetur adipiscing elit,</p>
    <div class="email-field">Enter your email
      <svg width="28" height="20" viewBox="0 0 28 20"><rect x="1" y="1" width="26" height="18" fill="none" stroke="#777" stroke-width="1.5"/><path d="M1 1l13 10L27 1M1 19l10-9M27 19l-10-9" fill="none" stroke="#777" stroke-width="1.2"/></svg>
    </div>
  </div>
  <div class="f-col f-links">
    <div class="f-head">Quick Links</div>
    <ul><li>Home</li><li>Events</li><li>About Us</li><li>Participation</li><li>Passengers</li><li>News</li><li>Volunteers</li><li>Contact Us</li></ul>
  </div>
  <div class="f-col f-connect">
    <div class="f-head">Connect With Us</div>
    <div class="boxes"><div></div><div></div></div>
  </div>
  <div class="f-bottom"><span>© 2017 Lindenkrügelhof</span><span>Privacy &amp; Cookies Policy</span></div>
</footer>

</body>
</html>
```